Digital Menu for New Picnic Company

We're in the process of creating a new picnic business called Cedar Hollow Hampers. We need our menu created as per the content in this google doc https://files.examplecloud.net/doc/7Kq2Rv9LmTzX4bWcYhJnPaE3sUd8FgVoNiQ5rMtLyKe/view?share=link
Please look at our website www.cedarhollowhampers.com.au to get an understanding of what we do and our branding style. We need the menu to be created matching the branding/colours as per our website however other than that please feel free to design it however you like and I will provide feedback from there. We are offering a high end gourmet product so the look and feel of the menu does need to reflect this.
PLEASE NOTE: This menu will only be displayed online as a PDF and doesn't need to be printed or provided physically.

```html
<!DOCTYPE html>
<html lang="en">
<head>
<meta charset="utf-8">
<title>Cedar Hollow Hampers – Gourmet Picnic Menu</title>
<link href="https://fonts.googleapis.com/css2?family=Oswald:wght@400;500&family=PT+Sans:wght@400;700&display=swap" rel="stylesheet">
<style>
:root{
  --stage:#808083;
  --paper:#ffffff;
  --paper-grain:#f1f2f4;
  --blue:#1f9bd7;
  --green:#7cc242;
  --ink:#2c2c2c;
  --white:#ffffff;
}
*{margin:0;padding:0;box-sizing:border-box}
html,body{width:1200px;height:890px;overflow:hidden;background:var(--stage)}
body{position:relative;font-family:"PT Sans",sans-serif;color:var(--ink)}
.top-strip{position:absolute;left:0;top:0;width:1200px;height:14px;background:#fff}
.bottom-strip{position:absolute;left:0;bottom:0;width:1200px;height:2px;background:#fff}
.page{position:absolute;top:102px;width:466px;height:659px;
  background:linear-gradient(90deg,var(--paper) 0%,var(--paper-grain) 30%,var(--paper) 55%,var(--paper-grain) 80%,var(--paper) 100%);
  box-shadow:3px 4px 8px rgba(0,0,0,.35);overflow:hidden}
.page--left{left:112px}
.page--right{left:638px;width:465px}
.hero{position:absolute;left:0;top:0;width:100%;height:240px}
.brand-badge{position:absolute;left:12px;top:123px;width:116px;height:116px;border-radius:50%;
  background:var(--blue);border:3px solid var(--white);display:flex;align-items:center;justify-content:center;text-align:center}
.brand-badge span{color:var(--white);font-family:"PT Sans",sans-serif;font-weight:700;font-size:15px;line-height:1.15;width:80px}
.intro{position:absolute;left:23px;top:260px;width:422px;font-size:8.6px;line-height:11.2px;text-align:justify}
.intro p{margin-bottom:11px}
.section{position:absolute}
.section h2{font-family:"Oswald",sans-serif;font-weight:400;color:var(--blue);font-size:13px;letter-spacing:-.3px;line-height:18px;margin-bottom:1px;white-space:nowrap}
.item{display:flex;font-size:8.9px;line-height:12.5px;white-space:nowrap}
.item .name{flex:1}
.item .price{font-weight:700;width:18px;text-align:left}
.divider{position:absolute;width:1px;background:#9a9a9a}
.choose{position:absolute;border-radius:50%;background:var(--blue);color:var(--white);
  font-family:"PT Sans",sans-serif;font-weight:700;text-align:center;display:flex;flex-direction:column;justify-content:center;
  box-shadow:2px 1px 0 var(--green)}
.choose--large{width:48px;height:48px;font-size:9.5px;line-height:11px}
.choose--small{width:32px;height:32px;font-size:5.6px;line-height:6.6px}
.footer{position:absolute;left:0;bottom:0;width:100%;height:45px;background:var(--blue);color:var(--white);text-align:center}
.footer .address{position:absolute;width:372px;top:8px;font-weight:700;font-size:12.5px;line-height:14px}
.footer .web{position:absolute;width:372px;top:25px;font-size:8.3px;line-height:10px}
.social{position:absolute;top:12px;width:22px;height:22px;border:1.3px solid var(--white);border-radius:50%}
</style>
</head>
<body>
<div class="top-strip"></div>
<div class="bottom-strip"></div>

<!-- Page one -->
<section class="page page--left">
  <svg class="hero" viewBox="0 0 466 240" role="img" aria-label="Photo of a grazing platter with cheeses, grapes and figs">
    <defs>
      <linearGradient id="heroA" x1="0" y1="0" x2="1" y2="1">
        <stop offset="0" stop-color="#8a5a3c"/>
        <stop offset=".35" stop-color="#d8c9a6"/>
        <stop offset=".7" stop-color="#f1ead6"/>
        <stop offset="1" stop-color="#b9b3a4"/>
      </linearGradient>
    </defs>
    <path d="M0 0H466V176Q300 245 70 196Q25 186 0 166Z" fill="url(#heroA)"/>
    <path d="M0 166Q25 186 70 196Q300 245 466 176" fill="none" stroke="#7cc242" stroke-width="4"/>
  </svg>
  <div class="brand-badge"><span>Cedar Hollow Hampers</span></div>

  <div class="intro">
    <p>Our Gourmet Picnics are handcrafted and delivered to your picnic spot on a wooden grazing tray. They come sealed in a catering box to ensure they are not tampered with. You then open the box and remove the grazing tray to enjoy the food. We prepare our food in accordance with food handling guidelines and all COVID precautions.</p>
    <p>We also provide complimentary beverages as part of the Gourmet Picnic being your choice of beers, wine or soft drink. You also can choose between still or sparkling water.</p>
    <p>As everyone has varying tastes, we have created our menu to be fully customisable so you can design your own picnic. We offer a wide variety of choices while focussing on quality ingredients for each component of your picnic.</p>
  </div>

  <div class="choose choose--large" style="left:405px;top:374px">CHOOSE<br>ANY 2</div>

  <div class="section" style="left:23px;top:412px;width:98px">
    <h2>CHEESE</h2>
    <div class="item"><span class="name">Creamy Blu</span><span class="price">$10</span></div>
    <div class="item"><span class="name">Blue Vein</span><span class="price">$10</span></div>
    <div class="item"><span class="name">Chilli Cream</span><span class="price">$10</span></div>
    <div class="item"><span class="name">Double Cream Brie</span><span class="price">$10</span></div>
    <div class="item"><span class="name">Camembert</span><span class="price">$10</span></div>
    <div class="item"><span class="name">Cheddar</span><span class="price">$10</span></div>
    <div class="item"><span class="name">Vintage Cheddar</span><span class="price">$10</span></div>
    <div class="item"><span class="name">Parmesan</span><span class="price">$10</span></div>
    <div class="item"><span class="name">Dutch Smoked</span><span class="price">$10</span></div>
    <div class="item"><span class="name">Goat Milk</span><span class="price">$10</span></div>
  </div>
  <div class="divider" style="left:137px;top:398px;height:192px"></div>

  <div class="section" style="left:159px;top:412px;width:126px">
    <h2>DIPS</h2>
    <div class="item"><span class="name">Mild Salsa</span><span class="price">$10</span></div>
    <div class="item"><span class="name">Spicy Salsa</span><span class="price">$10</span></div>
    <div class="item"><span class="name">Avocado</span><span class="price">$10</span></div>
    <div class="item"><span class="name">Hommus</span><span class="price">$10</span></div>
    <div class="item"><span class="name">Sweet Potato</span><span class="price">$10</span></div>
    <div class="item"><span class="name">Caramelised Onion</span><span class="price">$10</span></div>
    <div class="item"><span class="name">Roast Capsicum</span><span class="price">$10</span></div>
    <div class="item"><span class="name">Caviar</span><span class="price">$10</span></div>
    <div class="item"><span class="name">Guacamole</span><span class="price">$10</span></div>
    <div class="item"><span class="name">Sweet Chilli &amp; Sour Cream</span><span class="price">$10</span></div>
    <div class="item"><span class="name">Cashews</span><span class="price">$10</span></div>
    <div class="item"><span class="name">Jalapeno</span><span class="price">$10</span></div>
  </div>
  <div class="divider" style="left:303px;top:398px;height:192px"></div>

  <div class="section" style="left:325px;top:412px;width:121px">
    <h2>CRACKERS</h2>
    <div class="item"><span class="name">Golden Rounds</span><span class="price">$10</span></div>
    <div class="item"><span class="name">Natural Artisan Crackers</span><span class="price">$10</span></div>
    <div class="item"><span class="name">Wheat Wheels</span><span class="price">$10</span></div>
    <div class="item"><span class="name">Flat bread</span><span class="price">$10</span></div>
    <div class="item"><span class="name">Chilli jam flat bread</span><span class="price">$10</span></div>
    <div class="item"><span class="name">Assorted crackers</span><span class="price">$10</span></div>
    <div class="item"><span class="name">Veggie crackers</span><span class="price">$10</span></div>
    <div class="item"><span class="name">Pita Crackers</span><span class="price">$10</span></div>
    <div class="item"><span class="name">Bread Sticks</span><span class="price">$10</span></div>
    <div class="item"><span class="name">Corn Chips</span><span class="price">$10</span></div>
    <div class="item"><span class="name">Bruschetta Toasts</span><span class="price">$10</span></div>
    <div class="item"><span class="name">Wafer Crackers</span><span class="price">$10</span></div>
    <div class="item"><span class="name">Rice Crisps</span><span class="price">$10</span></div>
  </div>

  <footer class="footer">
    <div class="address" style="left:46px">PO Box 1187 Ashgrove Ridge NSW 2790</div>
    <div class="web" style="left:46px">www.cedarhollowhampers.com.au &nbsp;|&nbsp; info@cedarhollowhampers.com.au</div>
    <span class="social" style="left:385px"></span>
    <span class="social" style="left:420px"></span>
  </footer>
</section>

<!-- Page two -->
<section class="page page--right">
  <svg class="hero" viewBox="0 0 465 240" role="img" aria-label="Photo of a picnic grazing board with cheeses, olives, wine glasses and greenery">
    <defs>
      <linearGradient id="heroB" x1="0" y1="0" x2="1" y2="1">
        <stop offset="0" stop-color="#3d3a2e"/>
        <stop offset=".4" stop-color="#6b6453"/>
        <stop offset=".65" stop-color="#c9b98f"/>
        <stop offset="1" stop-color="#3f6b34"/>
      </linearGradient>
    </defs>
    <path d="M0 0H465V172Q300 245 70 196Q25 186 0 166Z" fill="url(#heroB)"/>
    <path d="M0 166Q25 186 70 196Q300 245 465 172" fill="none" stroke="#7cc242" stroke-width="4"/>
  </svg>
  <div class="brand-badge"><span>Cedar Hollow Hampers</span></div>

  <div class="choose choose--small" style="left:102px;top:233px">CHOOSE<br>ANY 3</div>
  <div class="section" style="left:21px;top:251px;width:108px">
    <h2>FRUIT</h2>
    <div class="item"><span class="name">Strawberrys</span><span class="price">$10</span></div>
    <div class="item"><span class="name">Grapes</span><span class="price">$10</span></div>
    <div class="item"><span class="name">Passion Fruit</span><span class="price">$10</span></div>
    <div class="item"><span class="name">Oranges</span><span class="price">$10</span></div>
    <div class="item"><span class="name">Kiwi Fruit</span><span class="price">$10</span></div>
  </div>

  <div class="choose choose--small" style="left:110px;top:370px">CHOOSE<br>ANY 1</div>
  <div class="section" style="left:21px;top:388px;width:108px">
    <h2>WATER PREFERENCE</h2>
    <div class="item"><span class="name">Still</span><span class="price">$10</span></div>
    <div class="item"><span class="name">Sparkling</span><span class="price">$10</span></div>
    <div class="item"><span class="name">Still &amp; Sparkling</span><span class="price">$10</span></div>
  </div>

  <div class="choose choose--small" style="left:102px;top:463px">CHOOSE<br>ANY 2</div>
  <div class="section" style="left:21px;top:481px;width:108px">
    <h2>WINE</h2>
    <div class="item"><span class="name">Champagne</span><span class="price">$10</span></div>
    <div class="item"><span class="name">Sauvignon Blanc</span><span class="price">$10</span></div>
    <div class="item"><span class="name">Chadonnay</span><span class="price">$10</span></div>
    <div class="item"><span class="name">Malbec</span><span class="price">$10</span></div>
    <div class="item"><span class="name">Shiraz</span><span class="price">$10</span></div>
    <div class="item"><span class="name">Cabernet Sauvignon</span><span class="price">$10</span></div>
    <div class="item"><span class="name">Merlot</span><span class="price">$10</span></div>
  </div>
  <div class="divider" style="left:148px;top:234px;height:360px"></div>

  <div class="choose choose--small" style="left:257px;top:233px">CHOOSE<br>ANY 1</div>
  <div class="section" style="left:158px;top:251px;width:121px">
    <h2>CHOCOLATES</h2>
    <div class="item"><span class="name">Hazel Pralines</span><span class="price">$10</span></div>
    <div class="item"><span class="name">Nougat Bar</span><span class="price">$10</span></div>
    <div class="item"><span class="name">Truffle Balls</span><span class="price">$10</span></div>
    <div class="item"><span class="name">Rocky Road</span><span class="price">$10</span></div>
    <div class="item"><span class="name">Wafer Fingers</span><span class="price">$10</span></div>
    <div class="item"><span class="name">Malt Balls</span><span class="price">$10</span></div>
    <div class="item"><span class="name">Milk Chocolate</span><span class="price">$10</span></div>
  </div>

  <div class="choose choose--small" style="left:258px;top:372px">CHOOSE<br>ANY 1</div>
  <div class="section" style="left:158px;top:390px;width:121px">
    <h2>BEER</h2>
    <div class="item"><span class="name">Craft Lager</span><span class="price">$10</span></div>
    <div class="item"><span class="name">Craft Pale Ale</span><span class="price">$10</span></div>
    <div class="item"><span class="name">Craft XPA</span><span class="price">$10</span></div>
    <div class="item"><span class="name">Australian Lager</span><span class="price">$10</span></div>
    <div class="item"><span class="name">Australian Dry</span><span class="price">$10</span></div>
    <div class="item"><span class="name">International Lager</span><span class="price">$10</span></div>
    <div class="item"><span class="name">Cider</span><span class="price">$10</span></div>
  </div>
  <div class="divider" style="left:303px;top:234px;height:360px"></div>

  <div class="choose choose--small" style="left:420px;top:230px">CHOOSE<br>ANY 1</div>
  <div class="section" style="left:314px;top:248px;width:129px">
    <h2>NON ALCOHOLIC</h2>
    <div class="item"><span class="name">Classic Cola</span><span class="price">$10</span></div>
    <div class="item"><span class="name">Cola No Sugar</span><span class="price">$10</span></div>
    <div class="item"><span class="name">Diet Cola</span><span class="price">$10</span></div>
    <div class="item"><span class="name">Cola Caffeine Free</span><span class="price">$10</span></div>
    <div class="item"><span class="name">Vanilla Cola</span><span class="price">$10</span></div>
    <div class="item"><span class="name">Brisk Cola</span><span class="price">$10</span></div>
    <div class="item"><span class="name">Brisk Max</span><span class="price">$10</span></div>
    <div class="item"><span class="name">Brisk Max Vanilla</span><span class="price">$10</span></div>
    <div class="item"><span class="name">Lemon Lime Soda</span><span class="price">$10</span></div>
    <div class="item"><span class="name">Orange Fizz</span><span class="price">$10</span></div>
    <div class="item"><span class="name">Citrus Rush</span><span class="price">$10</span></div>
    <div class="item"><span class="name">Lemon Squash</span><span class="price">$10</span></div>
    <div class="item"><span class="name">Lemon Squash Zero</span><span class="price">$10</span></div>
    <div class="item"><span class="name">Orange Soda</span><span class="price">$10</span></div>
    <div class="item"><span class="name">Orange Soda Zero</span><span class="price">$10</span></div>
    <div class="item"><span class="name">Apple Cider</span><span class="price">$10</span></div>
    <div class="item"><span class="name">Ginger Beer</span><span class="price">$10</span></div>
    <div class="item"><span class="name">Diet Ginger Beer</span><span class="price">$10</span></div>
    <div class="item"><span class="name">Lemon Lime &amp; Bitters</span><span class="price">$10</span></div>
    <div class="item"><span class="name">Creaming Soda</span><span class="price">$10</span></div>
    <div class="item"><span class="name">Sugar Free Creaming Soda</span><span class="price">$10</span></div>
  </div>

  <footer class="footer">
    <div class="address" style="left:14px">PO Box 1187 Ashgrove Ridge NSW 2790</div>
    <div class="web" style="left:14px">www.cedarhollowhampers.com.au &nbsp;|&nbsp; info@cedarhollowhampers.com.au</div>
    <span class="social" style="left:354px"></span>
    <span class="social" style="left:389px"></span>
  </footer>
</section>
</body>
</html>
```